Harborline Ventures

I provide collision estimating for autobody shops, so when they need a collision estimate and they are too busy or don't have the software, i write that estimate for them. I do this either in person or virtual. I need a postcard mailer design, 6.25 x 9 inches, with a header that reads HARBORLINE VENTURES, highlighting 20+ years of experience, and text that reads ASK ABOUT OUR TRAINING

Target Market(s)

Autobody Repair shops

Industry/Entity Type

Autobody

```html
<!DOCTYPE html>
<html lang="en">
<head>
<meta charset="utf-8">
<title>Harborline Ventures – Postcard Mailer</title>
<link rel="stylesheet" href="https://fonts.googleapis.com/css2?family=Oswald:wght@400;500;700&family=Roboto:wght@400;500;700&display=swap">
<style>
  :root{
    --red:#e3241b;
    --orange:#f26a1b;
    --black:#111111;
    --ink:#1c1c1c;
    --white:#ffffff;
    --grey:#d9d9d9;
    --line:#b9b9b9;
    --page:#eeeeee;
  }
  *{margin:0;padding:0;box-sizing:border-box}
  html,body{width:1200px;height:2460px;overflow:hidden;background:var(--page)}
  body{position:relative;font-family:'Roboto',sans-serif;color:var(--ink)}
  .card{position:absolute;left:50px;width:1100px;height:764px;background:var(--white);overflow:hidden;box-shadow:0 6px 24px rgba(0,0,0,.18)}
  .card--front{top:406px}
  .card--back{top:1290px}
  .abs{position:absolute}
  .heading{font-family:'Oswald',sans-serif;font-weight:700;text-transform:uppercase;line-height:1}
  .brand-name{font-family:'Oswald',sans-serif;font-weight:700;font-size:26px;letter-spacing:1px;color:var(--white);text-transform:uppercase}
  .photo{background:linear-gradient(135deg,#3a3a3a,#8e8e8e 55%,#d4d4d4)}
  .thumb{background:linear-gradient(135deg,#6d6d6d,#c9c9c9)}
  .caption{background:var(--red);color:var(--white);font-family:'Oswald',sans-serif;font-weight:500;font-size:15px;text-align:center;line-height:26px;letter-spacing:.5px;text-transform:uppercase}
  .badge{width:160px;height:160px}
  .badge svg{position:absolute;inset:0;width:100%;height:100%}
  .badge__text{position:absolute;inset:0;display:flex;flex-direction:column;align-items:center;justify-content:center;color:var(--white);font-family:'Oswald',sans-serif;text-transform:uppercase;text-align:center}
  .badge__num{font-size:46px;font-weight:700;line-height:1}
  .badge__label{font-size:14px;font-weight:500;line-height:1.15}
  .contact{display:flex;align-items:center;gap:12px}
  .contact__icon{width:32px;height:32px;border-radius:50%;background:var(--red);display:flex;align-items:center;justify-content:center;flex:none}
  .contact__icon svg{width:18px;height:18px}
  .phone{font-family:'Oswald',sans-serif;font-weight:700;font-size:40px;line-height:1}
  .email{font-size:19px}
  .web{font-family:'Oswald',sans-serif;font-weight:700;font-size:26px;letter-spacing:1px;color:var(--white)}
  .web span{color:var(--red)}
  .training{font-family:'Oswald',sans-serif;font-weight:700;font-size:30px;color:var(--red);text-transform:uppercase}
  .about-text{color:#e6e6e6;font-size:15.5px;line-height:1.55}
  .stamp{background:var(--grey)}
  .address-line{height:2px;background:var(--line)}
</style>
</head>
<body>
<svg width="0" height="0" style="position:absolute">
  <defs>
    <symbol id="burst" viewBox="0 0 150 150">
      <polygon points="150,75 137.8,91.8 140,112.5 121,121 112.5,140 91.8,137.8 75,150 58.2,137.8 37.5,140 29,121 10,112.5 12.2,91.8 0,75 12.2,58.2 10,37.5 29,29 37.5,10 58.2,12.2 75,0 91.8,12.2 112.5,10 121,29 140,37.5 137.8,58.2"/>
    </symbol>
    <symbol id="icon-phone" viewBox="0 0 24 24">
      <path fill="#fff" d="M6.6 10.8a15.1 15.1 0 0 0 6.6 6.6l2.2-2.2c.3-.3.7-.4 1-.2 1.1.4 2.3.6 3.6.6.6 0 1 .4 1 1V20c0 .6-.4 1-1 1A17 17 0 0 1 3 4c0-.6.4-1 1-1h3.5c.6 0 1 .4 1 1 0 1.3.2 2.5.6 3.6.1.3 0 .7-.2 1z"/>
    </symbol>
    <symbol id="icon-mail" viewBox="0 0 24 24">
      <path fill="#fff" d="M3 5h18v14H3z"/>
      <path fill="none" stroke="#e3241b" stroke-width="2" d="M3 6l9 7 9-7"/>
    </symbol>
  </defs>
</svg>

<!-- FRONT -->
<section class="card card--front">
  <svg class="abs" style="left:0;top:0" width="560" height="110" viewBox="0 0 560 110">
    <polygon points="0,0 420,0 380,70 0,70" fill="var(--red)"/>
    <polygon points="420,0 470,0 430,70 380,70" fill="var(--orange)"/>
    <polygon points="0,70 380,70 372,84 0,84" fill="var(--black)"/>
  </svg>
  <div class="abs brand-name" style="left:36px;top:18px">Harborline Ventures</div>

  <div class="abs heading" style="left:40px;top:120px;font-size:80px;color:var(--red)">Harborline</div>
  <div class="abs heading" style="left:40px;top:205px;font-size:100px;color:var(--black)">Ventures</div>
  <div class="abs heading" style="left:42px;top:320px;font-size:32px;color:var(--red)">Virtual or in person</div>
  <div class="abs heading" style="left:42px;top:358px;font-size:26px;color:var(--black);font-weight:500">To suit your needs</div>

  <div class="abs heading" style="left:40px;top:440px;font-size:48px;color:var(--red)">Services</div>
  <div class="abs heading" style="left:40px;top:494px;font-size:44px;color:var(--black);font-weight:500">We provide</div>

  <div class="abs thumb" role="img" aria-label="Photo of a consulting meeting at a desk" style="left:40px;top:572px;width:150px;height:104px"></div>
  <div class="abs caption" style="left:40px;top:676px;width:150px">Consulting</div>
  <div class="abs thumb" role="img" aria-label="Photo of a handshake partnership" style="left:200px;top:572px;width:150px;height:104px"></div>
  <div class="abs caption" style="left:200px;top:676px;width:150px">Partnership</div>
  <div class="abs thumb" role="img" aria-label="Photo of an estimate being written on paperwork" style="left:360px;top:572px;width:150px;height:104px"></div>
  <div class="abs caption" style="left:360px;top:676px;width:150px">Estimating</div>

  <div class="abs photo" role="img" aria-label="Photo of hands sheltering a model car on a desk" style="left:550px;top:0;width:550px;height:470px"></div>

  <div class="abs badge" style="left:560px;top:380px">
    <svg fill="var(--black)"><use href="#burst"/></svg>
    <div class="badge__text"><span class="badge__num">20+</span><span class="badge__label">Years of<br>experience</span></div>
  </div>

  <div class="abs training" style="left:745px;top:492px">Ask about our training</div>
  <div class="abs contact" style="left:745px;top:540px">
    <span class="contact__icon"><svg><use href="#icon-phone"/></svg></span>
    <span class="phone">(555) 214-7730</span>
  </div>
  <div class="abs contact" style="left:745px;top:598px">
    <span class="contact__icon"><svg><use href="#icon-mail"/></svg></span>
    <span class="email">info@harborlineventures.com</span>
  </div>

  <svg class="abs" style="left:530px;top:704px" width="570" height="60" viewBox="0 0 570 60">
    <polygon points="30,0 570,0 570,60 0,60" fill="var(--black)"/>
    <polygon points="30,0 70,0 40,60 0,60" fill="var(--red)"/>
  </svg>
  <div class="abs web" style="left:640px;top:716px">www.<span>harborlineventures</span>.com</div>
</section>

<!-- BACK -->
<section class="card card--back">
  <div class="abs" style="left:0;top:0;width:560px;height:764px;background:var(--black)"></div>
  <svg class="abs" style="left:420px;top:0" width="140" height="60" viewBox="0 0 140 60">
    <polygon points="40,0 140,0 140,60 0,60" fill="var(--red)"/>
  </svg>

  <div class="abs heading" style="left:40px;top:36px;font-size:56px;color:var(--white)">About <span style="color:var(--red)">us</span></div>
  <div class="abs" style="left:40px;top:104px;width:90px;height:5px;background:var(--red)"></div>
  <p class="abs about-text" style="left:40px;top:126px;width:480px">With over two decades of experience in the collision industry, we have helped countless body shops keep their workflow moving. When your team is too busy or lacks estimating software, we step in and write accurate, detailed estimates for you. Whether you prefer virtual support or an in-person visit, our goal is to save you time, reduce backlog and help your shop grow with confidence.</p>

  <div class="abs thumb" role="img" aria-label="Photo of a damaged vehicle in a repair bay" style="left:40px;top:330px;width:154px;height:92px"></div>
  <div class="abs thumb" role="img" aria-label="Photo of a technician inspecting a car" style="left:203px;top:330px;width:154px;height:92px"></div>
  <div class="abs thumb" role="img" aria-label="Photo of a collision estimate on a laptop" style="left:366px;top:330px;width:154px;height:92px"></div>
  <div class="abs thumb" role="img" aria-label="Photo of a repaired car body panel" style="left:40px;top:430px;width:154px;height:92px"></div>
  <div class="abs thumb" role="img" aria-label="Photo of an autobody shop interior" style="left:203px;top:430px;width:154px;height:92px"></div>

  <div class="abs badge" style="left:380px;top:432px">
    <svg fill="var(--red)"><use href="#burst"/></svg>
    <div class="badge__text"><span class="badge__num">20+</span><span class="badge__label">Years of<br>experience</span></div>
  </div>

  <div class="abs training" style="left:40px;top:560px">Ask about our training</div>
  <div class="abs contact" style="left:40px;top:608px;color:var(--white)">
    <span class="contact__icon"><svg><use href="#icon-phone"/></svg></span>
    <span class="phone">(555) 214-7730</span>
  </div>
  <div class="abs contact" style="left:40px;top:662px;color:var(--white)">
    <span class="contact__icon"><svg><use href="#icon-mail"/></svg></span>
    <span class="email">info@harborlineventures.com</span>
  </div>

  <svg class="abs" style="left:0;top:706px" width="560" height="58" viewBox="0 0 560 58">
    <polygon points="0,0 530,0 560,58 0,58" fill="var(--red)"/>
  </svg>
  <div class="abs web" style="left:40px;top:717px">www.harborlineventures.com</div>

  <div class="abs" style="left:640px;top:40px;padding:10px 22px;background:var(--red)">
    <span class="brand-name">Harborline Ventures</span>
  </div>
  <div class="abs stamp" style="left:960px;top:36px;width:104px;height:120px"></div>

  <div class="abs address-line" style="left:620px;top:420px;width:440px"></div>
  <div class="abs address-line" style="left:620px;top:480px;width:440px"></div>
  <div class="abs address-line" style="left:620px;top:540px;width:440px"></div>
  <div class="abs address-line" style="left:620px;top:600px;width:440px"></div>
</section>
</body>
</html>
```